Swimming Pool Service business card needed!!!! Please

Hi Everyone! Thanks for looking at my contest. I PROMISE to provide excellent feedback during this process.

I am starting a new swimming pool cleaning business in San Diego, California and would like your help in making a business card for me.

I like easy to read, classy and sophisticated.

I am having a website designed and I'm looking for it to have pictures of really clean & clear pools.

I really like the blue on white color format, but open to other colors.

I do not have a logo, but the name of my company is GLIMMERTIDE POOL SERVICE.

My tag line is: Pools so clean, you can see yourself "in" them. (does not need to have the quotes around "in"...maybe just italics for this word IN?) You decide for me.

I would like to have a logo designed that incorporates some sort of easy to read letters. I do not want cursive (handwriting) letters. I thought about having a "reflection" of letters (mirror image), but think that this will be hard to read from far away. Maybe you can surprise me and come up with an idea that works using the a mirror image....but I'm not sure. I was leaning toward plain old BLOCK letters as I think it would be easy to read on my truck.

I would like to have the NAQTR and WBK logos on the back of the card. I have attached those two as files. You can put other things on the back as well, but I need these two logos on there. Or maybe put them on the front of the card if you have a better idea for the back of the card! :-)

Maybe blue on the back of the card and white on the front of the card? I don't know, I'm just thinking out loud.

I had another card done awhile ago called HARBORLINE TEES. I have uploaded a copy of that card for your reference. I don't want this card to be the same as my new company is a swimming pool cleaning company, but I wanted you to see what I liked in the past.

THANK YOU!!!!
Updates

Reason: Partner out of town and want their feedback....so need more time to decide and designs still coming in.

Industry/Entity Type

Business

Contact Information for Business Card

GLIMMERTIDE POOL SERVICE
Dale Wexby
Owner
4817 Quarry Bend Ave. #512
San Diego, CA 92417
858-291-6083
www.glimmertidepoolservice.example

Font styles to use
Sans Serif

Colors
0255a3
3176b5
ffffff

Requirements
Nice to have
• Some things to (possibly) add to back of card (in no particular order)
• WBK logo
• NAQTR logo
• Free Estimates
• Residential and Commercial Services
• Equipment Repairs
• Saltwater Systems
• Licensed, Bonded, Insured
• Family Owned and Operated
• No Contracts
• =======================
• Check out the FolioMint business card that i attached.
• i think they did this using a chrome overlay.
• Can any of you guys design that? or is that done at my printer?
• ==================
Should not have
• Hi Designers-
• The first round of cards came back and let's stay away from the light blue (powder blue) color. I don't like the look of it on the business cards.
• Also, the pool company JPG's that I attached are other logos of pool companies that I liked. I don't want them to be on my card. The only logos that should be on my card are the one you are going to come up with for my company, the WBK logo and the NAQTR logo.
• Lastly, no vertical cards and no split cards (logo on left, contact info on right side).
• Thanks much!

```html
<!DOCTYPE html>
<html lang="en">
<head>
<meta charset="utf-8">
<title>Glimmertide Pool Service – Business Card</title>
<link rel="stylesheet" href="https://fonts.googleapis.com/css2?family=Orbitron:wght@700;900&display=swap">
<style>
  :root {
    --navy: #252262;
    --blue: #0e77bd;
    --white: #ffffff;
    --backdrop: #e9eaee;
    --badge-orange: #e8692a;
    --badge-blue: #1a5a9c;
  }
  html, body {
    margin: 0;
    width: 1200px;
    height: 1000px;
    overflow: hidden;
    background: var(--backdrop);
    font-family: "Orbitron", sans-serif;
  }
  .canvas { position: relative; width: 1200px; height: 1000px; }
  .card {
    position: absolute;
    width: 720px;
    height: 420px;
    background: var(--white);
    overflow: hidden;
    box-shadow: 0 6px 18px rgba(0,0,0,0.18);
  }
  .card-front { left: 80px; top: 70px; }
  .card-back { left: 400px; top: 520px; }
  .front-bands { position: absolute; inset: 0; }
  .brand {
    position: absolute;
    left: 46px;
    top: 42px;
    width: 470px;
    color: var(--navy);
    font-weight: 900;
    text-transform: uppercase;
    line-height: 1;
  }
  .brand-name { display: block; font-size: 46px; letter-spacing: 1px; }
  .brand-sub { display: block; font-size: 24px; text-align: right; margin-top: 4px; letter-spacing: 1px; }
  .contact {
    position: absolute;
    left: 58px;
    top: 222px;
    color: var(--white);
    font-weight: 700;
  }
  .contact-name { margin: 0; font-size: 30px; font-weight: 900; }
  .contact-role { margin: 4px 0 0; font-size: 21px; }
  .contact-details { margin: 36px 0 0; font-size: 16px; line-height: 1.5; font-style: normal; }
  .web {
    position: absolute;
    left: 0;
    right: 0;
    top: 118px;
    text-align: center;
    color: var(--navy);
    font-weight: 900;
    font-size: 24px;
    text-transform: uppercase;
    letter-spacing: 0.5px;
  }
  .credentials {
    position: absolute;
    left: 0;
    right: 0;
    top: 255px;
    display: flex;
    justify-content: center;
    gap: 18px;
  }
  .credential { width: 84px; height: 84px; border-radius: 50%; }
  .credential-assoc { background: linear-gradient(var(--badge-orange) 0 55%, var(--blue) 55% 100%); }
  .credential-operator { background: var(--badge-blue); }
</style>
</head>
<body>
<main class="canvas">
  <section class="card card-front" aria-label="Business card front">
    <svg class="front-bands" viewBox="0 0 720 420" width="720" height="420" aria-hidden="true">
      <polygon points="0,160 720,142 720,188 0,182" fill="var(--blue)"/>
      <polygon points="0,180 720,188 720,420 0,420" fill="var(--navy)"/>
    </svg>
    <h1 class="brand">
      <span class="brand-name">Glimmertide</span>
      <span class="brand-sub">Pool Service</span>
    </h1>
    <div class="contact">
      <p class="contact-name">Dale Wexby</p>
      <p class="contact-role">Owner</p>
      <address class="contact-details">
        4817 Quarry Bend Ave. #512<br>
        San Diego, CA 92417<br>
        858-291-6083
      </address>
    </div>
  </section>

  <section class="card card-back" aria-label="Business card back">
    <p class="web">glimmertidepoolservice.example</p>
    <div class="credentials">
      <div class="credential credential-assoc" role="img" aria-label="NAQTR association badge"></div>
      <div class="credential credential-operator" role="img" aria-label="WBK certified operator badge"></div>
    </div>
  </section>
</main>
</body>
</html>
```